MOSLEN Environmental needs an upgrade to its current business cards design

We need an upgrade to our current business cards design, where the MOSLEN acronym is included, as possible and not being overloaded.
MOSLEN Environmental is an Environmental Consultancy Firm based in Sydney.
We would like to see creative designs different from the standard type of business cards (for example, rounded edges, different to standard size of common business cards.

Target Market(s)

industrial companies (oil & gas, petrochemical, mining, insolvency, finance and manufacturing), developers, architect firms, law firms.

Industry/Entity Type

Business

Contact Information for Business Card

logos (brand and acronym), if they don't appear overloaded.
name
role
name of company (MOSLEN Environmental),
address (Level 3, Suite 3C, 47-49 Dorrigan Lane, Wexmoor, NSW, 2188) landline (02 7314 2986)
mobile (staff member)
email (staff member) and
website (www.moslengreen.example).
Include: Contaminated Land, Site Remediation, Groundwater Assessment, Health and Ecological Risk Assessments, Acid Sulfate Soils, Waste Classification.

Font styles to use
Serif
Sans Serif

Requirements
Must have
• A creative design different to the standard type of business cards.
Nice to have
• Rounded edges
• Different size of business cards rather than the standard size.
Should not have
• Preferable not to use white colour background, unless it is required from a creative design proposed.
• Not an overloaded design.
• Avoid black colours

```html
<!DOCTYPE html>
<html lang="en">
<head>
<meta charset="utf-8">
<title>MOSLEN Environmental – Business Cards</title>
<link href="https://fonts.googleapis.com/css2?family=Arimo:wght@400;700&display=swap" rel="stylesheet">
<style>
  :root {
    --canvas-bg: #d9cdb6;
    --card-black: #0c0c0c;
    --card-black-soft: #1c1c1c;
    --brand-green: #7fd332;
    --band-white: #f4f4f4;
    --text-light: #f2f2f2;
  }
  * { box-sizing: border-box; margin: 0; padding: 0; }
  html, body {
    width: 1200px; height: 802px; overflow: hidden;
    background: var(--canvas-bg);
    font-family: "Arimo", Arial, sans-serif;
  }
  .stage { position: relative; width: 1200px; height: 802px; }

  .card {
    position: absolute;
    left: 240px;
    width: 720px; height: 340px;
    border-radius: 22px;
    overflow: hidden;
    background: linear-gradient(135deg, var(--card-black-soft) 0%, var(--card-black) 45%, var(--card-black) 100%);
    box-shadow: 0 6px 18px rgba(0,0,0,0.25);
  }
  .card--services { top: 40px; }
  .card--contact { top: 422px; }

  .card__bands { position: absolute; inset: 0; width: 100%; height: 100%; }

  .brand {
    position: absolute;
    left: 56px; top: 134px;
    display: flex; align-items: flex-start; gap: 12px;
    color: var(--brand-green);
    font-weight: 700;
    font-size: 32px;
    line-height: 36px;
    letter-spacing: 0.5px;
  }
  .brand__mark {
    width: 16px; height: 16px;
    margin-top: 10px;
    background: var(--brand-green);
    flex: none;
  }
  .brand__name { display: block; white-space: nowrap; }

  .services {
    position: absolute;
    left: 366px; top: 96px;
    list-style: none;
    color: var(--text-light);
    font-weight: 700;
    font-size: 15px;
    line-height: 24px;
  }
  .services li { display: flex; align-items: center; gap: 8px; white-space: nowrap; }
  .services li::before {
    content: ""; width: 6px; height: 6px; border-radius: 50%;
    background: var(--brand-green); flex: none;
  }

  .divider {
    position: absolute;
    left: 380px; top: 60px;
    width: 1px; height: 220px;
    background: var(--brand-green);
  }

  .contact {
    position: absolute;
    left: 404px; top: 58px;
    color: var(--text-light);
    font-size: 15px;
    line-height: 20px;
  }
  .contact__name {
    color: var(--brand-green);
    font-weight: 700;
    font-size: 25px;
    line-height: 30px;
  }
  .contact__group { margin-top: 18px; }
  .contact__label { color: var(--brand-green); display: inline-block; width: 22px; }
  .contact__address { margin-top: 18px; }
</style>
</head>
<body>
<main class="stage">

  <section class="card card--services" aria-label="Card back: services">
    <svg class="card__bands" viewBox="0 0 720 340" preserveAspectRatio="none" aria-hidden="true">
      <polygon points="0,0 340,0 318,16 0,16" fill="var(--brand-green)"/>
      <polygon points="340,0 720,0 720,7 331,7" fill="var(--band-white)"/>
      <polygon points="0,332 410,332 420,340 0,340" fill="var(--band-white)"/>
      <polygon points="440,324 720,324 720,340 424,340" fill="var(--brand-green)"/>
    </svg>
    <div class="brand"><span class="brand__mark"></span><span><span class="brand__name">MOSLEN</span><span class="brand__name">Environmental</span></span></div>
    <ul class="services">
      <li>Contaminated Land</li>
      <li>Site Remediation</li>
      <li>Groundwater Assessment</li>
      <li>Health and Ecological Risk Assessments</li>
      <li>Acid Sulfate Soils</li>
      <li>Waste Classification</li>
    </ul>
  </section>

  <section class="card card--contact" aria-label="Card front: contact details">
    <svg class="card__bands" viewBox="0 0 720 340" preserveAspectRatio="none" aria-hidden="true">
      <polygon points="0,0 360,0 351,8 0,8" fill="var(--band-white)"/>
      <polygon points="380,0 720,0 720,16 358,16" fill="var(--brand-green)"/>
      <polygon points="0,324 320,324 342,340 0,340" fill="var(--brand-green)"/>
      <polygon points="320,333 720,333 720,340 330,340" fill="var(--band-white)"/>
    </svg>
    <div class="brand"><span class="brand__mark"></span><span><span class="brand__name">MOSLEN</span><span class="brand__name">Environmental</span></span></div>
    <div class="divider"></div>
    <div class="contact">
      <p class="contact__name">Marcus Delane</p>
      <p class="contact__role">Project Engineer</p>
      <p><span class="contact__label">M.</span>0412 587 306</p>
      <div class="contact__group">
        <p><span class="contact__label">T.</span>02 7314 2986</p>
        <p><span class="contact__label">W.</span>www.moslengreen.example</p>
        <p><span class="contact__label">E.</span>marcus@moslengreen.example</p>
      </div>
      <div class="contact__address">
        <p>Level 3, Suite 3C</p>
        <p>47-49 Dorrigan Lane</p>
        <p>Wexmoor, NSW, 2188</p>
      </div>
    </div>
  </section>

</main>
</body>
</html>
```